Business card for a new cabinet shop company named Torvane Cabinets for high end cabinets

Design a business card, thinking dark rich green with colours to speak of high end luxury ie; cream, gold, black possibly

Miles Harwick
Director Craftsman
Email: info@torvanecabinets.com.au
Instagram : @torvane.cabinets

```html
<!DOCTYPE html>
<html lang="en">
<head>
<meta charset="utf-8">
<title>Torvane Cabinets – Business Card</title>
<link rel="stylesheet" href="https://fonts.googleapis.com/css2?family=Josefin+Sans:wght@300;400;600&display=swap">
<style>
  :root {
    --stage: #e4e2de;
    --card: #0e0e0e;
    --card-edge: #c9a45c;
    --gold: #c9a45c;
    --ink-light: #f2f0ea;
    --ink-soft: #d9d6cf;
  }
  * { box-sizing: border-box; margin: 0; padding: 0; }
  html, body {
    width: 1200px; height: 800px; overflow: hidden;
    background: var(--stage);
    font-family: "Josefin Sans", "Helvetica Neue", Arial, sans-serif;
  }
  .sheet {
    width: 1200px; height: 800px;
    display: flex; align-items: center; justify-content: center; gap: 60px;
  }
  .card {
    position: relative;
    width: 525px; height: 300px;
    background: linear-gradient(160deg, #161616 0%, var(--card) 60%);
    border-radius: 18px;
    box-shadow: 0 0 0 3px var(--card-edge), 0 18px 40px rgba(0,0,0,.25);
    overflow: hidden;
    color: var(--ink-light);
  }
  .brand {
    display: flex; align-items: center; gap: 14px;
  }
  .brand-mark {
    width: 34px; height: 34px; border-radius: 50%;
    border: 2px solid var(--gold); flex: none;
  }
  .brand-name {
    color: var(--gold); font-weight: 400;
    font-size: 34px; letter-spacing: 1px; line-height: 1;
  }

  /* front */
  .card--front .brand { position: absolute; left: 0; right: 0; top: 100px; justify-content: center; }
  .hours {
    position: absolute; left: 0; right: 0; top: 200px;
    text-align: center; font-size: 12px; letter-spacing: 1.4px; text-transform: uppercase;
    line-height: 1.6;
  }
  .hours__week { color: var(--ink-light); }
  .hours__closed { color: var(--gold); font-weight: 600; }

  /* back */
  .card--back .brand { position: absolute; right: 36px; top: 62px; }
  .card--back .brand-name { font-size: 30px; }
  .rule {
    position: absolute; right: 36px; top: 128px;
    width: 290px; height: 0; border-top: 1.5px solid var(--gold);
  }
  .social {
    position: absolute; right: 36px; top: 142px;
    display: flex; align-items: center; gap: 8px;
    font-size: 12px; color: var(--ink-soft); letter-spacing: .6px;
  }
  .social__dot { width: 10px; height: 10px; border: 1.5px solid var(--gold); border-radius: 50%; }
  .person { position: absolute; left: 36px; bottom: 66px; }
  .person__name { font-size: 24px; font-weight: 600; letter-spacing: 2px; color: var(--ink-light); }
  .person__role { font-size: 12px; color: var(--gold); letter-spacing: 1px; margin-top: 4px; }
  .email {
    position: absolute; left: 36px; bottom: 32px;
    display: flex; align-items: center; gap: 10px;
    font-size: 12px; color: var(--ink-soft); letter-spacing: .6px;
  }
</style>
</head>
<body>
<main class="sheet">
  <section class="card card--front" aria-label="Business card front">
    <div class="brand">
      <span class="brand-mark"></span>
      <span class="brand-name">Torvane Cabinets</span>
    </div>
    <p class="hours">
      <span class="hours__week">Monday to Friday - 9:00 AM - 5:00 PM</span><br>
      <span class="hours__closed">Saturday / Sunday Closed</span>
    </p>
  </section>

  <section class="card card--back" aria-label="Business card back">
    <div class="brand">
      <span class="brand-mark"></span>
      <span class="brand-name">Torvane Cabinets</span>
    </div>
    <div class="rule"></div>
    <p class="social"><span class="social__dot"></span>Instagram : @torvane.cabinets</p>
    <div class="person">
      <p class="person__name">Miles Harwick</p>
      <p class="person__role">Director Craftsman</p>
    </div>
    <p class="email">
      <svg width="14" height="10" viewBox="0 0 14 10" aria-hidden="true">
        <rect x="0.75" y="0.75" width="12.5" height="8.5" fill="none" stroke="#c9a45c" stroke-width="1.3"/>
        <path d="M1 1 L7 6 L13 1" fill="none" stroke="#c9a45c" stroke-width="1.3"/>
      </svg>
      Email: info@torvanecabinets.com.au
    </p>
  </section>
</main>
</body>
</html>
```